We need a fresh, new church business card!!

We need a church business card with basic info to hand out as invites. We are looking for something clean that communicates our basic information clearly.

We are open to square or rectangle card sizes.

The attached logo is the only one that I have available. We'd like to see options with with text of the logo lighter and on a dark background as well as options with white/light backgrounds.

Also, we'd like to see option with rounded corners.

• Address - 2738 Larkmoor Ave., Millbrook, IL 61208
• Website - brookvale.church
• Phone - 815-392-6157
• Service times -
• Sunday - 10am Sunday School
• - 11am Family Worship
• - 6pm Night of Prayer
• Wednesday - 7:30pm Adult Bible Study
• Classes for all ages

```html
<!DOCTYPE html>
<html lang="en">
<head>
<meta charset="utf-8">
<title>Brookvale Pentecostal Church – Business Card</title>
<link rel="stylesheet" href="https://fonts.googleapis.com/css2?family=Open+Sans:wght@400;600;700&display=swap">
<style>
  :root {
    --stage: #2b2b2b;
    --card: #050505;
    --teal: #5b9aa9;
    --white: #f4f4f4;
    --grey: #8c8c8c;
    --band: #7d7d7d;
    --ghost: #11181b;
  }
  * { margin: 0; padding: 0; box-sizing: border-box; }
  html, body { width: 1200px; height: 900px; overflow: hidden; }
  body {
    background: var(--stage);
    font-family: "Open Sans", sans-serif;
    position: relative;
  }
  .card {
    position: absolute;
    left: 260px;
    width: 680px;
    height: 390px;
    background: var(--card);
    border-radius: 26px;
    overflow: hidden;
    box-shadow: 0 18px 40px rgba(0,0,0,.45);
  }
  .card--back { top: 45px; }
  .card--front { top: 465px; }

  /* Back side */
  .back-brand {
    position: absolute;
    top: 70px; left: 0; right: 0;
    display: flex; flex-direction: column; align-items: center; gap: 14px;
  }
  .back-brand .dot {
    width: 90px; height: 90px; border-radius: 50%;
    background: var(--teal);
  }
  .back-brand .name {
    color: var(--teal); font-weight: 600; font-size: 22px; letter-spacing: 3px;
  }
  .schedule {
    position: absolute;
    top: 245px; left: 0; right: 0;
    display: flex; justify-content: center; gap: 34px;
    font-size: 17px; line-height: 1.28; color: var(--white);
  }
  .schedule h3 {
    color: var(--teal); font-weight: 400; font-size: 17px; letter-spacing: .5px;
  }
  .schedule .sunday { text-align: right; }

  /* Front side */
  .ghost-mark {
    position: absolute;
    right: -40px; top: 30px;
    width: 300px; height: 300px; border-radius: 50%;
    background: var(--ghost);
  }
  .side-band {
    position: absolute;
    left: 58px; top: 0; bottom: 0; width: 30px;
    background: var(--band);
  }
  .front-brand {
    position: absolute;
    left: 44px; top: 70px;
    display: flex; align-items: center; gap: 18px;
  }
  .front-brand .dot {
    width: 58px; height: 58px; border-radius: 50%;
    background: var(--teal);
    border: 4px solid var(--card);
  }
  .front-brand .name {
    color: var(--grey); font-weight: 400; font-size: 34px; letter-spacing: 2px; line-height: 1.05;
  }
  .front-brand .name span { display: block; font-size: 15px; letter-spacing: 4.5px; }
  .contact {
    position: absolute;
    left: 220px; top: 185px;
    color: var(--white); font-size: 17px; line-height: 1.35;
  }
  .contact .person { font-weight: 700; font-size: 26px; letter-spacing: .5px; line-height: 1.1; }
  .contact .role { color: var(--teal); font-size: 16px; letter-spacing: 1px; margin-bottom: 4px; }
  .contact .line { display: flex; align-items: center; gap: 9px; }
  .contact svg { width: 13px; height: 13px; fill: var(--teal); flex: none; }
</style>
</head>
<body>

<section class="card card--back" aria-label="Card back">
  <div class="back-brand">
    <div class="dot"></div>
    <div class="name">BROOKVALE</div>
  </div>
  <div class="schedule">
    <div class="sunday">
      <h3>SERVICE TIMES:</h3>
      <p>Sunday - 10am Sunday School</p>
      <p>11am Family Worship</p>
      <p>6pm Night of Prayer</p>
    </div>
    <div class="wednesday">
      <h3>WEDNESDAY:</h3>
      <p>7:30pm Adult Bible Study</p>
      <p>Classes for all ages</p>
    </div>
  </div>
</section>

<section class="card card--front" aria-label="Card front">
  <div class="ghost-mark"></div>
  <div class="side-band"></div>
  <div class="front-brand">
    <div class="dot"></div>
    <div class="name">BROOKVALE<span>PENTECOSTAL CHURCH</span></div>
  </div>
  <div class="contact">
    <p class="person">DANA WHITFIELD</p>
    <p class="role">DIRECTOR</p>
    <p>2738 Larkmoor Ave.,</p>
    <p>Millbrook, IL 61208</p>
    <p class="line">
      <svg viewBox="0 0 24 24"><path d="M6.6 10.8a15.1 15.1 0 0 0 6.6 6.6l2.2-2.2a1 1 0 0 1 1-.25 11.4 11.4 0 0 0 3.6.57 1 1 0 0 1 1 1V20a1 1 0 0 1-1 1A17 17 0 0 1 3 4a1 1 0 0 1 1-1h3.5a1 1 0 0 1 1 1c0 1.250.2 2.450.57 3.57a1 1 0 0 1-.25 1z"/></svg>
      815-392-6157
    </p>
    <p class="line">
      <svg viewBox="0 0 24 24"><path d="M12 2a10 10 0 1 0 0 20 10 10 0 0 0 0-20zm6.9 6h-2.9a15.6 15.6 0 0 0-1.4-3.6A8 8 0 0 1 18.9 8zM12 4a14 14 0 0 1 1.9 4h-3.8A14 14 0 0 1 12 4zM4.3 14a8.2 8.2 0 0 1 0-4h3.4a16.5 16.5 0 0 0 0 4zm.8 2h2.9a15.6 15.6 0 0 0 1.4 3.6A8 8 0 0 1 5.1 16zM8 8H5.1a8 8 0 0 1 4.3-3.6A15.6 15.6 0 0 0 8 8zm4 12a14 14 0 0 1-1.9-4h3.8A14 14 0 0 1 12 20zm2.3-6H9.7a14.7 14.7 0 0 1 0-4h4.6a14.7 14.7 0 0 1 0 4zm.3 5.6a15.6 15.6 0 0 0 1.4-3.6h2.9a8 8 0 0 1-4.3 3.6zm1.7-5.6a16.5 16.5 0 0 0 0-4h3.4a8.2 8.2 0 0 1 0 4z"/></svg>
      www.brookvale.church
    </p>
  </div>
</section>

</body>
</html>
```